bag of mini candy bars

I already have the logo. I need a bag of 8 small candy bar minis with a clean design. Logo uploaded

Target Market(s)

Grocery retail

Industry/Entity Type

Food

Font styles to use
Serif
Sans Serif

Colors
FFF300
FFF600
FEFA6F
FFFEC7
FFFEE8
FFC000
F8CF3A
FAE287
FDF2CF
FEFAEE

```html
<!DOCTYPE html>
<html lang="en">
<head>
<meta charset="UTF-8">
<title>Marla's Organics – Caramel Nougat Mini Bars Pouch</title>
<link rel="stylesheet" href="https://fonts.googleapis.com/css2?family=Montserrat:wght@500;600;700;800&display=swap">
<style>
  :root {
    --bg: #e9e9e9;
    --pouch-white: #f7f7f5;
    --brand-yellow: #dcbb2a;
    --tag-yellow: #e0c02f;
    --choc-brown: #5b301b;
    --new-red: #d8262b;
    --white: #ffffff;
  }
  * { box-sizing: border-box; margin: 0; padding: 0; }
  html, body {
    width: 1200px; height: 900px; overflow: hidden;
    background: var(--bg);
    font-family: "Montserrat", sans-serif;
  }
  .canvas { position: relative; width: 1200px; height: 900px; }
  .pouch {
    position: absolute; left: 320px; top: 50px;
    width: 560px; height: 800px;
  }
  .pouch-shape { position: absolute; inset: 0; }
  .freshness-tag {
    position: absolute; left: 30px; top: 26px;
    width: 140px; height: 150px;
    background: var(--tag-yellow);
    color: var(--white);
    display: flex; flex-direction: column; justify-content: center; align-items: center;
    text-align: center; line-height: 1.15;
  }
  .freshness-tag .small { font-size: 11px; font-weight: 600; letter-spacing: .3px; }
  .freshness-tag .big { font-size: 18px; font-weight: 700; margin: 2px 0; }
  .brand-name {
    position: absolute; left: 0; right: 0; top: 250px;
    text-align: center;
    font-size: 56px; font-weight: 800;
    color: var(--choc-brown);
    letter-spacing: -1px;
    white-space: nowrap;
  }
  .count-title {
    position: absolute; left: 0; right: 90px; top: 390px;
    text-align: center;
    font-size: 46px; font-weight: 800;
    color: var(--choc-brown);
    white-space: nowrap;
  }
  .count-subtitle {
    position: absolute; left: 0; right: 90px; top: 452px;
    text-align: center;
    font-size: 12px; font-weight: 600;
    color: var(--brand-yellow);
    line-height: 1.4; letter-spacing: .3px;
    white-space: nowrap;
  }
  .cert-badge {
    position: absolute; left: 412px; top: 440px;
    width: 100px; height: 100px; border-radius: 50%;
    border: 4px solid var(--brand-yellow);
    background: var(--white);
    z-index: 2;
  }
  .product-window {
    position: absolute; left: 34px; top: 520px;
    width: 492px; height: 165px; border-radius: 26px;
    background: linear-gradient(120deg, #e8e5da 0%, #d9c278 45%, #9a6a43 75%, #6d3f22 100%);
  }
  .new-flag {
    position: absolute; left: 18px; top: 500px;
    padding: 8px 14px; border-radius: 18px 18px 18px 4px;
    background: var(--new-red); color: var(--white);
    font-size: 15px; font-weight: 700;
    border: 3px solid var(--white);
    z-index: 2;
  }
  .flavor-name {
    position: absolute; left: 40px; top: 702px;
    font-size: 19px; font-weight: 800; line-height: 1.15;
    color: var(--choc-brown);
  }
  .claims {
    position: absolute; left: 190px; top: 700px;
    display: flex; gap: 22px; align-items: center;
  }
  .claim { display: flex; align-items: center; gap: 7px; color: var(--choc-brown); }
  .claim svg { width: 30px; height: 30px; }
  .claim .divider { width: 1.5px; height: 30px; background: var(--choc-brown); }
  .claim .label { font-size: 13px; line-height: 1.2; }
  .claim .label b { font-weight: 700; display: block; }
  .net-weight {
    position: absolute; left: 0; right: 0; top: 760px;
    text-align: center;
    font-size: 14px; font-weight: 700; letter-spacing: .3px;
    color: var(--choc-brown);
  }
</style>
</head>
<body>
<div class="canvas">
  <div class="pouch">
    <svg class="pouch-shape" viewBox="0 0 560 800" width="560" height="800" aria-hidden="true">
      <path d="M14 0 H546 Q560 0 560 14 V786 Q560 800 546 800 H14 Q0 800 0 786 V14 Q0 0 14 0 Z" fill="var(--pouch-white)"/>
      <path d="M0 600 Q280 650 560 590 V786 Q560 800 546 800 H14 Q0 800 0 786 Z" fill="var(--brand-yellow)"/>
      <rect x="225" y="52" width="110" height="22" rx="11" fill="#c9c9c9"/>
      <line x1="0" y1="160" x2="560" y2="160" stroke="#e1e1de" stroke-width="3"/>
    </svg>

    <div class="freshness-tag">
      <span class="small">INDIVIDUALLY</span>
      <span class="big">WRAPPED</span>
      <span class="small">FOR FRESHNESS</span>
    </div>

    <div class="brand-name">Marla's Organics</div>

    <div class="count-title">8 MINI BARS</div>
    <div class="count-subtitle">INDIVIDUALLY WRAPPED FOR FRESHNESS<br>AND CONVENIENCE</div>

    <div class="cert-badge" role="img" aria-label="Organic certification badge"></div>

    <div class="product-window" role="img" aria-label="Window showing wrapped mini bars and two chocolate caramel nougat bars"></div>
    <div class="new-flag">NEW</div>

    <div class="flavor-name">CARAMEL<br>NOUGAT</div>

    <div class="claims">
      <div class="claim">
        <svg viewBox="0 0 30 30" fill="none" stroke="currentColor" stroke-width="2" stroke-linecap="round">
          <path d="M15 28 V12"/>
          <path d="M15 12 Q9 10 9 3 Q15 5 15 12 Q15 5 21 3 Q21 10 15 12"/>
          <path d="M15 20 Q8 20 5 14 Q12 13 15 20 Q18 13 25 14 Q22 20 15 20"/>
        </svg>
        <span class="divider"></span>
        <span class="label"><b>100%</b>Organic</span>
      </div>
      <div class="claim">
        <svg viewBox="0 0 30 30" fill="none" stroke="currentColor" stroke-width="2" stroke-linecap="round">
          <path d="M15 3 V7"/>
          <path d="M6 13 Q6 7 15 7 Q24 7 24 13 Z"/>
          <path d="M8 13 Q8 24 15 27 Q22 24 22 13"/>
        </svg>
        <span class="divider"></span>
        <span class="label"><b>100%</b>Vegan</span>
      </div>
      <div class="claim">
        <svg viewBox="0 0 30 30" fill="none" stroke="currentColor" stroke-width="2" stroke-linecap="round">
          <circle cx="15" cy="15" r="13"/>
          <path d="M15 24 V9"/>
          <path d="M15 14 Q11 13 11 9 Q15 10 15 14 Q15 10 19 9 Q19 13 15 14"/>
          <path d="M15 20 Q11 19 11 15 Q15 16 15 20 Q15 16 19 15 Q19 19 15 20"/>
          <path d="M6 6 L24 24"/>
        </svg>
        <span class="divider"></span>
        <span class="label"><b>Gluten</b>Free</span>
      </div>
    </div>

    <div class="net-weight">NET WEIGHT: 7.5 OZ (250 GM)</div>
  </div>
</div>
</body>
</html>
```